Dawson's Lawn Service needs a postcard design

I need a design to attract lawn cutting customers. I am a high school junior, focusing on my city and the neighboring city. I think it would be advantageous to let my potential clients know I am earning money for my college education. They should also know, I will be working side by side with my father, who operated his own lawn service for 20 years, so they can be assured of a quality result for their lawn. I will be using state of the art, commercial equipment.

A few things that are unique to my service are; my mower weighs half of what other commercial mowers do (a softer footprint), my mower does NOT throw clippings into mulch or flower beds, at an additional charge I offer bagging of the clippings and/or dog waste clean-up. I am thinking about a two-sided design. I would also like a cartoon style picture of myself riding my mower. If this is something you can create, I can send you a photo of myself and a photo of my mower. If not, I can get this drawing done separately, then send it to you, I would just need to know what kind of file you would need it in. I am not going to have a business name, I want to introduce myself as Dawson to keep it simple and personal. We can add a coupon to the postcard, offering one free cut with commitment to a full 26 week season. The name of my high school is Marwick High.

The cartoon picture attached is our logo.

Target Market(s)

Homeowners that use a commercial lawn cutting service, homeowners that need a temporary service while they are on vacation

Industry/Entity Type

School

Colors
3176b5
9bcb3c

Requirements
Must have
• An appeal for people to want to help me earn money for my college education. A clear idea they will be getting top notch service. I definitely want a drawing of myself on my mower. Phone # 555-271-0936
• design must work with parcelrelay.com/routeblanketmail guidelines

```html
<!DOCTYPE html>
<html lang="en">
<head>
<meta charset="utf-8">
<title>Dawson Lawn Cutting Service – Postcard Front</title>
<link rel="stylesheet" href="https://fonts.googleapis.com/css2?family=Open+Sans:ital,wght@0,300;0,400;0,700;1,700&family=PT+Serif:ital@0;1&display=swap">
<style>
  :root {
    --sky: #29a9e1;
    --grass: #1d9a3c;
    --grass-light: #3cb54a;
    --grass-dark: #0f7a2c;
    --lime: #9bcb3c;
    --ink: #1e2a3a;
    --white: #ffffff;
    --stage: #ecebe7;
    --panel: #4a4d4f;
  }
  * { margin: 0; padding: 0; box-sizing: border-box; }
  html, body { width: 1200px; height: 982px; overflow: hidden; background: var(--stage); }
  .postcard {
    position: absolute; left: 50px; top: 33px; width: 1090px; height: 840px;
    background: var(--white); overflow: hidden;
    box-shadow: 0 4px 14px rgba(0,0,0,.18);
    font-family: "Open Sans", Arial, sans-serif;
  }
  .header-flag { position: absolute; left: 0; top: 0; width: 704px; height: 210px; }
  .header-text {
    position: absolute; left: 34px; top: 46px; color: var(--white);
    font-weight: 700; font-size: 29px; line-height: 41px;
  }
  .brand { position: absolute; left: 660px; top: 70px; display: flex; align-items: center; gap: 16px; }
  .brand-dot { width: 86px; height: 86px; border-radius: 50%; background: var(--lime); }
  .brand-name { color: var(--sky); font-weight: 400; line-height: 1; }
  .brand-name .big { display: block; font-size: 78px; }
  .brand-name .small { display: block; font-size: 24px; margin-top: 6px; padding-left: 14px; }
  .greeting-band {
    position: absolute; left: 0; top: 223px; width: 100%; height: 71px;
    background: linear-gradient(90deg, var(--grass-dark), var(--grass-light) 50%, var(--grass-dark));
    color: var(--white); font-family: "PT Serif", Georgia, serif; font-style: italic;
    font-size: 38px; text-align: center; line-height: 71px;
  }
  .lawn-scene {
    position: absolute; left: 0; top: 302px; width: 558px; height: 378px;
    background: linear-gradient(180deg, #c9ccd0 0%, #dfe2e4 30%, #8fa37a 48%, #4f7d33 62%, #6aa23d 100%);
  }
  .services {
    position: absolute; left: 558px; top: 302px; width: 532px; height: 378px;
    background: linear-gradient(135deg, #5d6062, var(--panel) 55%, #3b3e40);
    color: var(--white);
  }
  .services-backdrop { position: absolute; inset: 0; }
  .services-title {
    position: absolute; left: 39px; top: 44px; font-family: "PT Serif", Georgia, serif;
    font-weight: 400; font-size: 27px; padding-bottom: 6px; border-bottom: 4px solid var(--grass-light);
  }
  .service-list { position: absolute; left: 22px; top: 92px; list-style: none; width: 500px; }
  .service-list li {
    position: relative; padding-left: 18px; font-weight: 300; font-size: 20px;
    line-height: 26px; margin-bottom: 20px;
  }
  .service-list svg { position: absolute; left: 0; top: 7px; width: 13px; height: 13px; }
  .offer-area {
    position: absolute; left: 0; top: 691px; width: 100%; height: 149px;
    background: linear-gradient(90deg, var(--grass-light), var(--grass) 60%, var(--grass-dark));
  }
  .offer-flag { position: absolute; left: 0; top: 691px; width: 860px; height: 73px; }
  .offer-text {
    position: absolute; left: 18px; top: 708px; color: var(--ink);
    font-weight: 700; font-style: italic; font-size: 28px;
  }
  .father-note {
    position: absolute; left: 8px; top: 776px; color: var(--white);
    font-family: "PT Serif", Georgia, serif; font-size: 20px; line-height: 27px;
  }
  .call {
    position: absolute; right: 20px; top: 716px; color: var(--white);
    font-family: "PT Serif", Georgia, serif; text-align: right;
  }
  .call-label { font-size: 35px; line-height: 44px; }
  .call-number {
    display: flex; align-items: center; justify-content: flex-end; gap: 6px;
    font-size: 38px; line-height: 48px; margin-top: 6px; white-space: nowrap;
  }
  .call-number svg { width: 32px; height: 32px; flex: none; }
</style>
</head>
<body>
  <main class="postcard">
    <svg class="header-flag" viewBox="0 0 704 210" aria-hidden="true">
      <polygon points="0,0 704,0 514,210 0,210" fill="var(--sky)"/>
    </svg>
    <div class="header-text">
      <div>Marwick High School Junior Student</div>
      <div>Earning Money For My College</div>
      <div>Education</div>
    </div>

    <div class="brand">
      <span class="brand-dot"></span>
      <div class="brand-name"><span class="big">Dawson</span><span class="small">Lawn Cutting Service</span></div>
    </div>

    <div class="greeting-band">Hi, All I Am Dawson</div>

    <div class="lawn-scene" role="img" aria-label="Cartoon of Dawson riding his mower in front of a house with a freshly cut lawn"></div>

    <section class="services">
      <div class="services-backdrop" role="img" aria-label="Faded background photo of a smiling family"></div>
      <h2 class="services-title">Service I Provide</h2>
      <ul class="service-list">
        <li><svg viewBox="0 0 14 14"><circle cx="7" cy="7" r="7" fill="var(--lime)"/><path d="M3.5 7.2l2.3 2.3 4.5-4.8" stroke="#fff" stroke-width="1.8" fill="none"/></svg>Assurnce of A Quality of Lawn Cutting Service</li>
        <li><svg viewBox="0 0 14 14"><circle cx="7" cy="7" r="7" fill="var(--lime)"/><path d="M3.5 7.2l2.3 2.3 4.5-4.8" stroke="#fff" stroke-width="1.8" fill="none"/></svg>My Mower Weighs Half Of What Other<br>Commercial Mowers Do</li>
        <li><svg viewBox="0 0 14 14"><circle cx="7" cy="7" r="7" fill="var(--lime)"/><path d="M3.5 7.2l2.3 2.3 4.5-4.8" stroke="#fff" stroke-width="1.8" fill="none"/></svg>My Mower Does Not Throw Clippings Into<br>Much Or Flower Beds</li>
        <li><svg viewBox="0 0 14 14"><circle cx="7" cy="7" r="7" fill="var(--lime)"/><path d="M3.5 7.2l2.3 2.3 4.5-4.8" stroke="#fff" stroke-width="1.8" fill="none"/></svg>At An Additional Charge I Offer Bagging of<br>The Clippings &amp;/ or Dog Waste Clean-up</li>
      </ul>
    </section>

    <div class="offer-area"></div>
    <svg class="offer-flag" viewBox="0 0 860 73" aria-hidden="true">
      <polygon points="0,0 860,0 812,73 0,73" fill="var(--white)"/>
      <polygon points="0,0 853,0 807,73 0,73" fill="var(--sky)"/>
    </svg>
    <p class="offer-text">Book Me &nbsp;&nbsp;for 26 Week Season &amp; GET One Cut FREE</p>
    <p class="father-note">I am Working Side By Side With My Father, Who Operats His Own<br>Lawn Cutting Service For 20 Years</p>

    <div class="call">
      <div class="call-label">Call Us Today</div>
      <div class="call-number">
        <svg viewBox="0 0 34 34" aria-hidden="true"><circle cx="17" cy="17" r="15" fill="none" stroke="#fff" stroke-width="2.5"/><path d="M11.5 9.5c1-.8 2-.6 2.6.4l1.4 2.6c.4.8.2 1.6-.5 2.1l-1 .8c.8 2 2.4 3.8 4.5 4.8l.9-1c.6-.7 1.4-.8 2.1-.4l2.6 1.5c.9.6 1 1.6.3 2.5-1.4 1.7-3.1 2.2-5.3 1.2-4-1.8-7.3-5.3-8.7-9.4-.6-2 0-3.7 1.1-5.1z" fill="#fff"/></svg>
        <span>555.271.0936</span>
      </div>
    </div>
  </main>
</body>
</html>
```